Brightwall Residences Estepona listings flyer

Brightwall Residences Estepona are a specialist estate agency focussed solely on selling modern and contemporary homes.

We need an A4 folded flyer to be designed so that Brightwall Residences Estepona can leaflet drop all of the modern homes for sale in our area to generate new instructions / listings. We need to engage with owners of those types of homes by posting this marketing material through their letter boxes in the hope that they see our funky and modern design and decide to call us about our services to sell their home, if for sale.

We would like to see sharp lines and a modern design (see our logo for style and colour scheme), with lots of white spaces and using photos which can blend in to the background to provide a powerful and impacting image to set us aside from any other direct mail leaflets which may be in their post box. It needs to show

* Quality
* Style
* Modern and forward thinking in design and outlook
* Professionalism

Front page
Top:
Logo of Brightwall Residences Estepona.
Guiding your sleek property to its buyer. Nothing else!

4 property photos in a grid position

Bottom banner
If you are thinking of selling, read on…

INSIDE LEFT & RIGHT (DOUBLE PAGE POSSIBLY BLANK WHITE BACKGROUND)
Title: Use Brightwall Residences Estepona – the specialist modern homes agency to sell your home

We bring an exciting and dynamic mix of modern marketing with good old fashioned service to guarantee only the most qualified clients will be viewing your home (use online marketing image)

Marketing packages include stylish online brochures, professional photography, stunning drone video footage, informative video walk thru’s and unique floor plans (use drone and floor plan images)

Targeted social media campaigns focusing on international clientele actively looking to buy property in southern Spain (use social media image)

Bespoke, powerful advertising packages enable worldwide exposure for both online and traditional channels to market. We can be as discreet or as visible as you want us to be to sell your home

During our 20 years on the Costa del Sol, we have built up an enviable network of collaborating agents meaning you only have to instruct one expert real estate agent, Brightwall Residences Estepona, to gain maximum exposure for your home

BACK PAGE

If you want service that matches the value of your home, contact us today for a private, personalised consultation. Brightwall Residences Estepona. Nothing else.

Suite 14
Torrevaca Office Park
Calle Los Almendros
Torrevaca, Marbella

Tel: +34 952 418 360
Mobil y Whatsapp: +34 687 530 271
Email: info@brightwallresidencesestepona.example
www.brightwallresidencesestepona.example

Target Market(s)

Wealthy property owners of contemporary and modern homes who are looking to sell their home

Industry/Entity Type

Real Estate Agent

Font styles to use
Serif
Sans Serif

Colors
606060
e7e7e7
f5f5f5

Requirements
Must have
• Classy, professional, modern design with the ability to stand out from other leaflet drops / direct mail in letter box
Nice to have
• straight lines to border photos
• Maybe extend the lines further than they should so it has the look of an architects plan
• Blend in images to white background in the middle open double page
Should not have
• Lots of different colours

```html
<!DOCTYPE html>
<html lang="en">
<head>
<meta charset="utf-8">
<title>Brightwall Residences Estepona – Flyer Cover</title>
<link rel="stylesheet" href="https://fonts.googleapis.com/css2?family=Lato:wght@300;400&display=swap">
<style>
  :root {
    --ink: #606060;
    --ink-soft: #7a7a7a;
    --headline: #8a8a8a;
    --band: #c9cacd;
    --paper: #f5f5f5;
    --page-bg: #e7e7e7;
    --frame: #ffffff;
    --photo-top: #7eaedc;
    --photo-bottom: #dce6ee;
  }
  * { margin: 0; padding: 0; box-sizing: border-box; }
  html, body { width: 1200px; height: 1134px; overflow: hidden; }
  body {
    background: var(--page-bg);
    font-family: "Lato", sans-serif;
    color: var(--ink);
    display: flex;
    align-items: center;
    justify-content: center;
  }
  .cover {
    position: relative;
    width: 800px;
    height: 1094px;
    background: linear-gradient(180deg, #ffffff 0%, var(--paper) 100%);
  }
  .cover__kicker {
    position: absolute;
    top: 92px; left: 0; right: 0;
    text-align: center;
    font-weight: 400;
    font-size: 27px;
    color: var(--ink-soft);
    letter-spacing: 0.2px;
  }
  .cover__headline {
    position: absolute;
    top: 142px; left: 0; right: 0;
    text-align: center;
    font-weight: 300;
    font-size: 86px;
    line-height: 1;
    text-transform: uppercase;
    color: var(--headline);
    letter-spacing: 1px;
  }
  .photo-band {
    position: absolute;
    top: 292px; left: 0;
    width: 100%;
    height: 540px;
    background: var(--band);
  }
  .photo {
    position: absolute;
    border: 4px solid var(--frame);
    background: linear-gradient(180deg, var(--photo-top) 0%, var(--photo-bottom) 100%);
  }
  .photo--terraces { top: 30px;  left: 32px;  width: 490px; height: 240px; }
  .photo--garden   { top: 16px;  left: 534px; width: 238px; height: 254px; }
  .photo--villa    { top: 282px; left: 48px;  width: 262px; height: 240px; }
  .photo--poolside { top: 268px; left: 322px; width: 462px; height: 254px; }
  .cover__footer {
    position: absolute;
    left: 0; right: 0; bottom: 0;
    height: 262px;
    display: flex;
    align-items: center;
    justify-content: space-between;
    padding: 0 60px 0 70px;
  }
  .brand {
    display: flex;
    align-items: center;
    gap: 16px;
    font-weight: 400;
    color: var(--ink);
  }
  .brand__mark {
    width: 22px; height: 22px;
    background: var(--ink);
  }
  .brand__name {
    font-size: 24px;
    line-height: 1.3;
    letter-spacing: 1.5px;
    text-transform: uppercase;
  }
  .cover__teaser {
    font-weight: 300;
    font-size: 28px;
    line-height: 1.3;
    color: var(--ink);
    text-align: left;
  }
</style>
</head>
<body>
  <main class="cover">
    <p class="cover__kicker">Guiding Your Sleek Property To Its Buyer.</p>
    <h1 class="cover__headline">Nothing Else!</h1>

    <section class="photo-band">
      <div class="photo photo--terraces" role="img" aria-label="Photo of white modern terraced apartments with lawn and pool"></div>
      <div class="photo photo--garden" role="img" aria-label="Photo of a white modern villa terrace with garden loungers"></div>
      <div class="photo photo--villa" role="img" aria-label="Photo of a contemporary white house with trees and pool"></div>
      <div class="photo photo--poolside" role="img" aria-label="Photo of a large modern villa behind a wide swimming pool"></div>
    </section>

    <footer class="cover__footer">
      <div class="brand">
        <span class="brand__mark"></span>
        <span class="brand__name">Brightwall Residences<br>Estepona</span>
      </div>
      <p class="cover__teaser">If you are thinking<br>of selling, read on…</p>
    </footer>
  </main>
</body>
</html>
```